Business Card for plorvaTEC

Create a Business Card with an existing logo for plorvaTEC AG. We are a Information Technology company that does consulting and developing SW to automate business processes. The main colors are given from the logo.

Industry/Entity Type

Business

Requirements
Nice to have
• we use a a font style Century Gothic in our documents

```html
<!DOCTYPE html>
<html lang="en">
<head>
<meta charset="utf-8">
<title>plorvaTEC Business Card</title>
<link href="https://fonts.googleapis.com/css2?family=Didact+Gothic&display=swap" rel="stylesheet">
<style>
  :root {
    --stage: #363634;
    --card: #ffffff;
    --pattern: #f4f2f2;
    --ink: #333333;
    --ink-soft: #666666;
    --blue-light: #8fbfea;
    --blue: #2f86cf;
    --green-light: #eef0a0;
    --green: #a9cc3a;
    --mark: #2f86cf;
  }
  * { margin: 0; padding: 0; box-sizing: border-box; }
  html, body {
    width: 1200px; height: 1000px; overflow: hidden;
    background: var(--stage);
    font-family: "Didact Gothic", "Century Gothic", sans-serif;
  }
  .canvas { position: relative; width: 1200px; height: 1000px; }
  .card {
    position: absolute; left: 98px; top: 175px;
    width: 1004px; height: 650px;
    background: var(--card); overflow: hidden;
  }
  .card-pattern {
    position: absolute; inset: 0;
    background: var(--pattern); opacity: 0.55;
  }
  .corner-art { position: absolute; }
  .corner-art--blue {
    left: 0; bottom: 0; width: 220px; height: 380px;
    background: radial-gradient(circle at 30% 55%, var(--blue-light), var(--blue) 75%);
  }
  .corner-art--green {
    right: 0; top: 0; width: 220px; height: 380px;
    background: radial-gradient(circle at 60% 50%, #fbfbe0, var(--green-light) 30%, var(--green) 85%);
  }
  .brand {
    position: absolute; left: 70px; top: 75px;
    display: flex; align-items: center; gap: 38px;
  }
  .brand-dot {
    width: 210px; height: 210px; border-radius: 50%;
    background: var(--mark);
  }
  .brand-name {
    font-size: 96px; color: var(--ink); letter-spacing: -1px; line-height: 1;
  }
  .contact {
    position: absolute; right: 86px; top: 388px;
    text-align: right; line-height: 1.12;
  }
  .contact-name, .contact-role { font-size: 36px; color: var(--ink); }
  .contact-phone { font-size: 40px; color: var(--ink-soft); margin-top: 20px; letter-spacing: 1px; }
  .contact-email { font-size: 36px; color: var(--ink-soft); margin-top: 2px; }
</style>
</head>
<body>
<main class="canvas">
  <section class="card">
    <div class="card-pattern" role="img" aria-label="faint repeating wave pattern across the card"></div>
    <div class="corner-art corner-art--blue" role="img" aria-label="blue decorative corner swoosh"></div>
    <div class="corner-art corner-art--green" role="img" aria-label="green decorative corner swoosh"></div>
    <div class="brand">
      <div class="brand-dot" aria-hidden="true"></div>
      <div class="brand-name">plorvaTEC</div>
    </div>
    <div class="contact">
      <div class="contact-name">Maren Volk</div>
      <div class="contact-role">Manager</div>
      <div class="contact-phone">07480 312 665</div>
      <div class="contact-email">marenvolk@plorvatec.com</div>
    </div>
  </section>
</main>
</body>
</html>
```